Business Card Design needed for logo design project

This project is linked to Logo: brand identity for modern furniture design studio..

Our company needs a Business Card Design. Please refer to our original project in the link above.

Industry/Entity Type

Business

```html
<!DOCTYPE html>
<html lang="en">
<head>
<meta charset="utf-8">
<title>Sofora business card</title>
<link href="https://fonts.googleapis.com/css2?family=Andika&display=swap" rel="stylesheet">
<style>
  :root {
    --backdrop: #e7e5e1;
    --card-light: #fafbfc;
    --card-tint: #eef3f3;
    --band-dark: #8a8a8a;
    --band-mid: #b4b4b4;
    --band-pale: #d2d2d2;
    --wordmark: #6e6e6e;
    --ink: #444444;
    --ink-soft: #4a4a4a;
    --paper: #ffffff;
  }
  html, body {
    margin: 0;
    padding: 0;
    width: 1013px;
    height: 1200px;
    overflow: hidden;
    background: var(--backdrop);
  }
  .canvas {
    position: relative;
    width: 1013px;
    height: 1200px;
    font-family: "Andika", sans-serif;
  }
  .card {
    position: absolute;
    display: block;
    box-shadow: 0 3px 10px rgba(0,0,0,0.18);
  }
  .card--front { left: 33px; top: 53px; width: 926px; height: 520px; }
  .card--back  { left: 53px; top: 631px; width: 923px; height: 520px; }
  .wordmark { font-family: "Andika", sans-serif; fill: var(--wordmark); font-weight: 400; }
  .holder-name { font-family: "Andika", sans-serif; fill: var(--paper); font-size: 38px; }
  .tagline { font-family: "Andika", sans-serif; fill: var(--ink-soft); font-size: 28px; }
  .contact-line { font-family: "Andika", sans-serif; fill: var(--ink-soft); font-size: 19px; letter-spacing: 1.5px; }
  .contact-icon { fill: var(--ink); }
  .divider { stroke: #6a6a6a; stroke-width: 2.5; }
</style>
</head>
<body>
<div class="canvas">

  <!-- Front of card -->
  <svg class="card card--front" viewBox="0 0 840 472" xmlns="http://www.w3.org/2000/svg">
    <defs>
      <linearGradient id="paperFront" x1="0" y1="0" x2="1" y2="1">
        <stop offset="0" stop-color="var(--card-light)"/>
        <stop offset="1" stop-color="var(--card-tint)"/>
      </linearGradient>
    </defs>
    <rect class="card-pattern" role="img" aria-label="Faint line drawings of armchairs scattered across the card" width="840" height="472" fill="url(#paperFront)"/>
    <rect class="brand-band" x="0" y="144" width="840" height="186" fill="var(--band-dark)"/>
    <ellipse class="brand-window" cx="429" cy="237" rx="217" ry="96" fill="var(--paper)"/>
    <text class="wordmark" x="429" y="275" font-size="118" text-anchor="middle">sofora</text>
  </svg>

  <!-- Back of card -->
  <svg class="card card--back" viewBox="0 0 838 472" xmlns="http://www.w3.org/2000/svg">
    <defs>
      <linearGradient id="paperBack" x1="0" y1="0" x2="1" y2="1">
        <stop offset="0" stop-color="var(--card-light)"/>
        <stop offset="1" stop-color="var(--card-tint)"/>
      </linearGradient>
    </defs>
    <rect class="card-pattern" role="img" aria-label="Faint line drawings of armchairs scattered across the card" width="838" height="472" fill="url(#paperBack)"/>

    <path class="logo-band" d="M0 78 Q145 140 290 80 L290 170 L0 170 Z" fill="var(--band-mid)"/>
    <path class="band-fold" d="M290 80 L352 44 L352 136 L290 170 Z" fill="var(--band-pale)"/>
    <rect class="name-band" x="352" y="44" width="486" height="92" fill="var(--band-dark)"/>

    <text class="wordmark" x="42" y="92" font-size="76">sofora</text>
    <text class="holder-name" x="820" y="103" text-anchor="end">[First and Last Name]</text>

    <line class="divider" x1="355" y1="145" x2="355" y2="472"/>

    <text class="tagline" x="95" y="266">[Text ........</text>
    <text class="tagline" x="95" y="304">............</text>
    <text class="tagline" x="95" y="342">..............Here]</text>

    <g class="contact-list">
      <!-- address -->
      <path class="contact-icon" d="M510 187 L527 201 L523 201 L523 214 L516 214 L516 206 L504 206 L504 214 L497 214 L497 201 L493 201 Z"/>
      <text class="contact-line" x="555" y="209">[Street Adderess]</text>
      <!-- phone -->
      <path class="contact-icon" d="M503 259 Q499 263 501 269 Q505 280 515 287 Q520 290 523 286 L525 283 L519 278 L516 281 Q510 277 507 270 L510 268 L506 261 Z"/>
      <text class="contact-line" x="555" y="278">[Phone Number]</text>
      <!-- email -->
      <path class="contact-icon" d="M496 336 L524 336 L510 346 Z M496 339 L496 351 L505 344 Z M524 339 L524 351 L515 344 Z M496 353 L507 346 L510 348 L513 346 L524 353 Z"/>
      <text class="contact-line" x="555" y="348">[Email Adderess]</text>
      <!-- website -->
      <path class="contact-icon" d="M497 400 L523 400 L523 416 L497 416 Z M500 403 L500 413 L520 413 L520 403 Z M493 418 L527 418 L525 422 L495 422 Z"/>
      <text class="contact-line" x="555" y="417">[Website]</text>
    </g>
  </svg>

</div>
</body>
</html>
```